New business card for civil engineering company - "Keystone Audit"

We need a business card designed for our new structural engineering company.

The company name is "Keystone Audit" logo files attached.

We would like the following:
* Two-sided card
* Simple design

Information to be placed on the card:
Name - Marcus Dellow
Job Title - Director / Structural Engineer
Credentials - BEng(Hons), CPEng, CMengNZ, IntPE(NZ)
Email - marcus.dellow@keystoneaudit.co.nz
mobile - 0219364058
website - www.keystoneaudit.co.nz

```html
<!DOCTYPE html>
<html lang="en">
<head>
<meta charset="utf-8">
<title>Keystone Audit — Business Card</title>
<link href="https://fonts.googleapis.com/css2?family=Rubik:wght@300;400;500;700&display=swap" rel="stylesheet">
<style>
  :root {
    --backdrop: #1d1d1f;
    --navy-top: #36608f;
    --navy-bottom: #274c77;
    --brand-blue: #4a8fc9;
    --paper: #efefef;
    --ink: #3a3a3c;
    --ink-navy: #1f4a7d;
    --white: #ffffff;
  }
  * { box-sizing: border-box; margin: 0; padding: 0; }
  html, body {
    width: 1200px; height: 897px; overflow: hidden;
    background: var(--backdrop);
    font-family: "Rubik", sans-serif;
  }
  .stage { position: relative; width: 1200px; height: 897px; }
  .card {
    position: absolute; top: 179px;
    width: 297px; height: 537px;
  }
  .card--front {
    left: 281px;
    background: linear-gradient(180deg, var(--navy-top), var(--navy-bottom));
  }
  .card--back {
    left: 628px;
    background: var(--paper);
    color: var(--ink);
  }
  .wordmark {
    position: absolute; display: flex; align-items: center; gap: 9px;
    font-weight: 500; letter-spacing: 2.5px; white-space: nowrap;
  }
  .wordmark__mark { width: 12px; height: 12px; background: var(--brand-blue); }
  .card--front .wordmark {
    left: 0; right: 0; top: 338px; justify-content: center;
    color: var(--white); font-size: 20px;
  }
  .card--back .wordmark {
    right: 32px; top: 172px; color: var(--ink); font-size: 18px;
  }
  .contact { position: absolute; left: 36px; top: 280px; right: 20px; }
  .contact__name {
    font-size: 19px; font-weight: 400; color: var(--ink-navy);
    letter-spacing: 0.3px; line-height: 1.1;
  }
  .contact__role { font-size: 14px; font-weight: 300; margin-top: 5px; }
  .contact__creds { font-size: 13px; font-weight: 300; margin-top: 8px; line-height: 1.3; }
  .contact__rule {
    width: 74px; height: 2px; background: var(--ink-navy);
    margin-top: 20px;
  }
  .contact__list { list-style: none; margin-top: 22px; font-size: 14px; font-weight: 300; }
  .contact__item { display: flex; align-items: center; gap: 8px; height: 23px; }
  .contact__icon { width: 18px; height: 16px; flex: none; }
  .contact__web { margin-top: 15px; font-size: 14px; font-weight: 300; }
  .contact__web strong { font-weight: 500; color: var(--ink-navy); }
</style>
</head>
<body>
<main class="stage">
  <section class="card card--front" aria-label="Card front">
    <div class="wordmark"><span class="wordmark__mark"></span>KEYSTONE AUDIT</div>
  </section>

  <section class="card card--back" aria-label="Card back">
    <div class="wordmark"><span class="wordmark__mark"></span>KEYSTONE AUDIT</div>
    <div class="contact">
      <h1 class="contact__name">MARCUS DELLOW</h1>
      <p class="contact__role">Director / Structural Engineer</p>
      <p class="contact__creds">BEng(Hons), CPEng, CMengNZ,<br>IntPE(NZ)</p>
      <div class="contact__rule"></div>
      <ul class="contact__list">
        <li class="contact__item">
          <svg class="contact__icon" viewBox="0 0 18 16" aria-hidden="true">
            <rect x="5" y="0.5" width="8" height="15" rx="1.5" fill="none" stroke="#3a3a3c" stroke-width="1"/>
            <line x1="5" y1="12" x2="13" y2="12" stroke="#3a3a3c" stroke-width="1"/>
          </svg>
          0219364058
        </li>
        <li class="contact__item">
          <svg class="contact__icon" viewBox="0 0 18 16" aria-hidden="true">
            <rect x="0.5" y="2.5" width="17" height="11" fill="none" stroke="#3a3a3c" stroke-width="1"/>
            <polyline points="0.5,2.5 9,9 17.5,2.5" fill="none" stroke="#3a3a3c" stroke-width="1"/>
          </svg>
          marcus.dellow@keystoneaudit.co.nz
        </li>
      </ul>
      <p class="contact__web">www.<strong>KEYSTONEAUDIT</strong>.co.nz</p>
    </div>
  </section>
</main>
</body>
</html>
```